Business Card desgin, company called Stand Fast.

I am looking for the logo colors (3) to be used on the card in whatever design you think might work. the certifications are on the back (4) on the front will be my name, Dana Whitlock, owner/instructor, phone 208.555.0193, website www.sfx-drills.example, email dw@sfx-drills.example. im flexible on fonts.

Target Market(s)

firearms owners

Industry/Entity Type

firearms training

Contact Information for Business Card

certification icons on back

```html
<!DOCTYPE html>
<html lang="en">
<head>
<meta charset="utf-8">
<title>Stand Fast — Business Card</title>
<link rel="stylesheet" href="https://fonts.googleapis.com/css2?family=Montserrat:wght@700&family=Arimo:wght@400;700&display=swap">
<style>
  :root {
    --bg: #989898;
    --navy: #0b2a42;
    --red: #c1272d;
    --white: #ffffff;
    --rule: #6f8194;
    --badge-light: #e9e4dc;
    --badge-dark: #1d2630;
    --badge-accent: #3d6f9c;
  }
  html, body {
    margin: 0;
    width: 1200px;
    height: 1000px;
    overflow: hidden;
    background: var(--bg);
  }
  .card {
    position: absolute;
    width: 694px;
    height: 400px;
    background: var(--navy);
    overflow: hidden;
  }
  .card-front { left: 253px; top: 68px; }
  .card-back  { left: 254px; top: 524px; }

  /* front */
  .front-mark {
    position: absolute;
    left: 289px; top: 108px;
    width: 116px; height: 116px;
  }
  .front-name {
    position: absolute;
    left: 0; right: 0; top: 236px;
    margin: 0;
    text-align: center;
    font: 700 50px/1 "Montserrat", sans-serif;
    color: var(--red);
    text-transform: uppercase;
  }
  .front-tagline {
    position: absolute;
    left: 0; right: 0; top: 294px;
    margin: 0;
    text-align: center;
    font: 400 18px/1 "Arimo", sans-serif;
    color: var(--white);
  }

  /* back */
  .brand {
    position: absolute;
    left: 37px; top: 57px;
    display: flex; align-items: center; gap: 9px;
  }
  .brand-dot {
    width: 50px; height: 50px;
    border: 4px solid var(--white);
    border-radius: 50%;
    box-sizing: border-box;
  }
  .brand-name {
    font: 700 26px/1 "Montserrat", sans-serif;
    color: var(--red);
    text-transform: uppercase;
  }
  .cert-badges {
    position: absolute;
    left: 396px; top: 58px;
    width: 262px; height: 52px;
  }
  .person-name {
    position: absolute;
    left: 37px; top: 242px;
    margin: 0;
    font: 700 24px/1 "Arimo", sans-serif;
    letter-spacing: 1px;
    color: var(--white);
  }
  .person-role {
    position: absolute;
    left: 38px; top: 274px;
    margin: 0;
    font: 400 11px/1 "Arimo", sans-serif;
    letter-spacing: 2px;
    color: var(--red);
    text-transform: uppercase;
  }
  .divider {
    position: absolute;
    left: 39px; top: 303px;
    width: 616px; height: 1px;
    background: var(--rule);
  }
  .contact-list {
    position: absolute;
    left: 38px; top: 320px;
    margin: 0; padding: 0; list-style: none;
    font: 400 18px/21px "Arimo", sans-serif;
    color: var(--white);
  }
  .contact-list li { display: flex; align-items: center; gap: 10px; }
  .contact-list svg { width: 13px; height: 13px; flex: none; }
  .website {
    position: absolute;
    right: 40px; top: 341px;
    margin: 0;
    font: 400 18px/21px "Arimo", sans-serif;
    color: var(--white);
  }
  .website strong { font-weight: 700; }
</style>
</head>
<body>

<section class="card card-front">
  <svg class="front-mark" viewBox="0 0 116 116" aria-hidden="true">
    <circle cx="58" cy="58" r="54" fill="none" stroke="var(--white)" stroke-width="7"/>
  </svg>
  <h1 class="front-name">Stand Fast</h1>
  <p class="front-tagline">Si Vis Pacem, Para Bellum</p>
</section>

<section class="card card-back">
  <div class="brand">
    <span class="brand-dot"></span>
    <span class="brand-name">Stand Fast</span>
  </div>

  <svg class="cert-badges" viewBox="0 0 262 52" role="img" aria-label="Four certification badges">
    <path d="M2 6 Q23 -2 44 6 L44 26 Q44 42 23 50 Q2 42 2 26 Z" fill="var(--badge-light)" stroke="#d77a2a" stroke-width="2"/>
    <path d="M60 2 H108 V30 L100 38 H68 L60 30 Z" fill="var(--badge-dark)"/>
    <rect x="56" y="32" width="56" height="8" rx="2" fill="var(--badge-accent)"/>
    <path d="M127 2 H177 V28 L168 40 H136 L127 28 Z" fill="var(--badge-dark)"/>
    <rect x="124" y="24" width="56" height="8" rx="2" fill="#e0a43a"/>
    <path d="M212 2 L224 6 V18 Q224 26 212 30 Q200 26 200 18 V6 Z" fill="var(--white)"/>
    <rect x="194" y="38" width="68" height="10" rx="1" fill="var(--white)" opacity="0.85"/>
  </svg>

  <h2 class="person-name">Dana Whitlock</h2>
  <p class="person-role">Owner/Instructor</p>
  <div class="divider"></div>

  <ul class="contact-list">
    <li>
      <svg viewBox="0 0 16 16" aria-hidden="true"><path d="M3.5 1 L6 1 L7 5 L5 6.5 Q6.5 9.5 9.5 11 L11 9 L15 10 L15 12.5 Q14 15 11 14.5 Q3 12 1.5 4 Q1.5 1.5 3.5 1 Z" fill="var(--white)"/></svg>
      <span>208.555.0193</span>
    </li>
    <li>
      <svg viewBox="0 0 16 16" aria-hidden="true"><rect x="1" y="3.5" width="14" height="10" fill="var(--white)"/><path d="M1 3.5 L8 9.5 L15 3.5" fill="none" stroke="var(--navy)" stroke-width="1.4"/></svg>
      <span>dw@sfx-drills.example</span>
    </li>
  </ul>

  <p class="website"><strong>sfx-drills</strong>.example</p>
</section>

</body>
</html>
```